Zerovan Medical

We are a medical supplier company we sell machines and equipment to all medical sectors in Iraq. Our services include not only the installation of these machines and equipment but also we provide support after installation and we train the staff to use these machines/equipment
We need a website that will make us stand out from our competitors, something professional and catchy
Starting from the home page, before showing the home page we want the loading screen to have our logo animated in a nice way
Then we can proceed to creating the other pages which are
Projects
Services
Training
About
and Contact us
Attached below is our logo and the color blue that we hope to use in the theme of the website
**** In the home page we want to focus on our partners and services****

Target Market(s)

Medical Sector

Industry/Entity Type

Medical

Coding

Coded - Design and coding required

Number of Pages Required

5+ page

Colors
0054AA
0677BA
7BADD7
CADEEF
E8F1F8

Requirements
Must have
• Animation in loading screen or animation in home page
Nice to have
• Some sort of animation for our partners

```html
<!DOCTYPE html>
<html lang="en">
<head>
<meta charset="utf-8">
<title>Zerovan Medical</title>
<link href="https://fonts.googleapis.com/css2?family=Poppins:wght@400;500;600;700&display=swap" rel="stylesheet">
<style>
:root{
  --navy:#24295e;
  --blue:#1b9ad6;
  --blue-deep:#0054aa;
  --blue-mid:#0677ba;
  --sky:#7badd7;
  --pale:#cadeef;
  --mist:#e8f1f8;
  --grey-bg:#f5f5f5;
  --text:#333;
  --muted:#8a8a8a;
  --black:#050505;
  --white:#fff;
}
*{box-sizing:border-box;margin:0;padding:0}
html,body{width:1200px;height:4851px;overflow:hidden}
body{position:relative;font-family:"Poppins",sans-serif;color:var(--text);background:var(--white)}
.abs{position:absolute}
.btn{position:absolute;display:flex;align-items:center;justify-content:center;color:var(--white);font-size:17px;font-weight:500}
.btn--navy{background:var(--navy)}
.btn--blue{background:var(--blue)}

/* top bar */
.topbar{left:396px;top:0;width:804px;height:30px;background:var(--blue);clip-path:polygon(0 0,100% 0,100% 100%,28px 100%);color:var(--white);font-size:13px}
.topbar span{position:absolute;top:6px;white-space:nowrap}
.social{position:absolute;top:9px;width:12px;height:12px;border-radius:50%;background:var(--white)}
.header{left:0;top:0;width:1200px;height:100px;border-bottom:1px solid #e5e5e5}
.brand{position:absolute;display:flex;align-items:center;gap:12px;font-weight:700;color:var(--navy);white-space:nowrap}
.brand__mark{width:56px;height:56px;border:5px solid var(--blue)}
.brand__name{font-size:32px;line-height:1}
.brand__tag{font-size:10px;letter-spacing:2px;font-weight:600;display:block;margin-top:4px}
.nav a{position:absolute;top:61px;font-size:15px;font-weight:500;color:#222;text-decoration:none}

/* hero */
.hero{left:0;top:100px;width:1200px;height:710px}
.hero__title{left:0;top:306px;width:1200px;text-align:center;color:var(--white);font-size:62px;font-weight:600;line-height:70px}
.hero__text{left:190px;top:474px;width:820px;text-align:center;color:var(--white);font-size:17px;line-height:22px}

/* about */
.about__media{left:77px;top:961px;width:445px;height:346px;background:linear-gradient(135deg,#d4e2ef,#9db5cd)}
.about__title{left:597px;top:990px;font-size:42px;font-weight:600;color:#111}
.about__text{left:597px;top:1062px;width:525px;font-size:13px;line-height:21.5px;color:var(--muted)}

/* sections */
.section-title{left:0;width:1200px;text-align:center;font-size:42px;font-weight:600;color:#111}
.services{left:0;top:1455px;width:1200px;height:623px;background:var(--grey-bg)}
.svc-img{position:absolute;top:1679px;width:247px;height:169px}
.svc-label{position:absolute;top:1837px;width:188px;height:51px;background:var(--white);display:flex;align-items:center;justify-content:center;font-size:18px;font-weight:500;color:#222}

.partners{left:0;top:2078px;width:1200px;height:797px;background:linear-gradient(180deg,#3aa7dd,#52b2e4 50%,#3ea3da)}
.partner{position:absolute;width:240px;height:184px;background:var(--white);text-align:center}
.partner__name{position:absolute;left:0;top:42px;width:100%;font-size:24px;font-weight:700;color:#b8262d;white-space:nowrap}
.partner__desc{position:absolute;left:15px;top:118px;width:210px;font-size:13px;line-height:21px;color:#333}

.project{position:absolute;top:3122px;width:341px;height:350px;background:#fafafa}
.project__img{width:341px;height:241px}
.project__text{padding:36px 16px 0;text-align:center;font-size:13px;line-height:21px;color:#444}
.dot{position:absolute;top:3558px;width:16px;height:16px}

.contact{left:57px;top:3732px;width:1070px;height:441px;box-shadow:0 4px 26px rgba(0,0,0,.08);background:var(--white)}
.contact__title{left:125px;top:3770px;font-size:35px;font-weight:600;color:#111}
.field{position:absolute;background:#eee;border:1px solid #e2e2e2;font-size:8px;color:#aaa;padding:9px 10px}

/* footer */
.footer__text{left:81px;top:4606px;width:310px;font-size:13px;line-height:15px;color:var(--white)}
.flink{position:absolute;left:546px;font-size:17px;color:var(--white)}
.flink::before{content:"›";color:var(--blue);font-size:24px;position:absolute;left:-3px;top:-9px}
.flink span{padding-left:24px}
.fcontact{position:absolute;left:908px;font-size:16px;color:var(--white);white-space:nowrap}
.footer__rule{left:81px;top:4755px;width:1020px;height:1px;background:#3a3a3a}
.footer__small{top:4794px;font-size:12px;color:var(--white)}
</style>
</head>
<body>

<!-- header -->
<header class="abs header">
  <div class="brand" style="left:28px;top:22px">
    <div class="brand__mark"></div>
    <div><span class="brand__name">Zerovan Medical</span><span class="brand__tag">FOR MEDICAL APPLIANCES</span></div>
  </div>
  <div class="abs topbar">
    <span style="left:90px">&#9742;&nbsp; +1 555-014-2290</span>
    <span style="left:290px">&#9993;&nbsp; hello@zerovanmed.example</span>
    <i class="social" style="left:672px"></i><i class="social" style="left:702px"></i><i class="social" style="left:732px"></i>
  </div>
  <nav class="nav">
    <a style="left:457px">Home</a><a style="left:555px">About</a><a style="left:653px">Services</a><a style="left:778px">Projects</a><a style="left:891px">Training</a>
  </nav>
  <div class="btn btn--navy" style="left:1044px;top:53px;width:109px;height:32px;font-size:13px">Contact Us</div>
</header>

<!-- hero -->
<section class="abs hero">
  <svg width="1200" height="710" role="img" aria-label="Photo of a hospital operating room with medical equipment">
    <defs>
      <linearGradient id="heroShade" x1="0" y1="0" x2="1" y2="1">
        <stop offset="0" stop-color="#6b6f73"/><stop offset=".5" stop-color="#4c5054"/><stop offset="1" stop-color="#35393c"/>
      </linearGradient>
    </defs>
    <rect width="1200" height="710" fill="url(#heroShade)"/>
    <path d="M0 590 C300 720 700 760 1200 600 L1200 710 L0 710Z" fill="var(--white)"/>
    <path d="M20 600 C350 730 800 740 1200 580 L1200 625 C820 780 380 760 20 600Z" fill="var(--navy)"/>
    <path d="M0 596 C320 735 800 745 1200 612 L1200 640 C800 760 340 760 0 610Z" fill="var(--blue)"/>
    <path d="M0 610 C320 752 800 755 1200 640 L1200 710 L0 710Z" fill="var(--white)"/>
  </svg>
</section>
<h1 class="abs hero__title">Zerovan For<br>Medical Appliances</h1>
<p class="abs hero__text">ZEROVAN MEDICAL Company is one of the specialized private companies in Iraq. Our job fields are lab. Diagnostics, equipment and medical appliances &amp; Ophthalmic Dept.</p>
<div class="btn btn--navy" style="left:448px;top:554px;width:153px;height:41px">Contact Us</div>
<div class="btn btn--blue" style="left:614px;top:554px;width:153px;height:41px">Our Projects</div>

<!-- about -->
<div class="abs about__media" role="img" aria-label="Photo of medical imaging equipment in a hospital room"></div>
<h2 class="abs about__title">About Us</h2>
<p class="abs about__text">ZEROVAN MEDICAL Company is one of the specialized private companies in Iraq. Our job fields are lab. Diagnostics, equipment and medical appliances &amp; Ophthalmic Dept. ZEROVAN MEDICAL Established to be able cover all over Iraq not only Kurdistan Region because our business expanded to be able cover all over Iraq through our three offices in Baghdad , Basra &amp; Najaf cities.</p>
<div class="btn btn--navy" style="left:597px;top:1208px;width:151px;height:39px">Read More</div>

<!-- services -->
<section class="abs services"></section>
<h2 class="abs section-title" style="top:1540px">Our Services</h2>
<div class="svc-img" style="left:60px;background:linear-gradient(#dfe7ef,#8ea2b6)" role="img" aria-label="Operating room equipment photo"></div>
<div class="svc-img" style="left:339px;background:linear-gradient(#f1f1f1,#9aa0a6)" role="img" aria-label="Technician installing a microscope photo"></div>
<div class="svc-img" style="left:618px;background:linear-gradient(#f0f2f4,#aab4bd)" role="img" aria-label="Patient monitor photo"></div>
<div class="svc-img" style="left:897px;background:linear-gradient(#cfd6dc,#4c5866)" role="img" aria-label="Staff training on equipment photo"></div>
<div class="svc-label" style="left:91px">Equipments</div>
<div class="svc-label" style="left:370px">Installation</div>
<div class="svc-label" style="left:647px">Training</div>
<div class="svc-label" style="left:927px">Maintenance</div>
<div class="btn btn--blue" style="left:526px;top:1963px;width:152px;height:40px">Read More</div>

<!-- partners -->
<section class="abs partners" role="img" aria-label="Blue tinted photo of a hospital ward"></section>
<h2 class="abs section-title" style="top:2166px;color:var(--white)">Our Partners</h2>
<div class="partner" style="left:73px;top:2297px"><div class="partner__name">Arcova</div><p class="partner__desc">Rapid tests using new technology instruments</p></div>
<div class="partner" style="left:350px;top:2297px"><div class="partner__name" style="color:#555">Pelmora</div><p class="partner__desc">Anesthesia ,Ventilator &amp; monitoring Equipment</p></div>
<div class="partner" style="left:622px;top:2297px"><div class="partner__name">Kestral Group</div><p class="partner__desc">Surgical Instruments and Equipment</p></div>
<div class="partner" style="left:895px;top:2297px"><div class="partner__name" style="color:#1c8a3a">Biolume</div><p class="partner__desc">Diode Laser Equipment</p></div>
<div class="partner" style="left:69px;top:2527px"><div class="partner__name" style="color:#2a3b9a">Vendra Lab</div><p class="partner__desc">Rapid tests using new technology instruments</p></div>
<div class="partner" style="left:346px;top:2527px"><div class="partner__name" style="color:#2a3b9a;font-size:21px;top:45px">Delsutra Medical</div><p class="partner__desc">Orthopedic drill Instrument</p></div>
<div class="partner" style="left:619px;top:2527px"><div class="partner__name" style="color:#c2272d">Esmira</div><p class="partner__desc">Ultrasound &amp; ECG Machines</p></div>
<div class="partner" style="left:893px;top:2527px"><div class="partner__name" style="color:#333">Norvanta</div><p class="partner__desc" style="top:124px">FOR Hospital Furniture</p></div>
<div class="btn btn--navy" style="left:526px;top:2779px;width:152px;height:38px">View All</div>

<!-- projects -->
<h2 class="abs section-title" style="top:2966px">Latest Projects</h2>
<div class="project" style="left:57px"><div class="project__img" style="background:linear-gradient(#e6e6e6,#8f949a)" role="img" aria-label="Laparoscope tower in a clinic photo"></div><p class="project__text">30 complete units of Laparoscope distributed among 20 hospitals in Whole Iraq.</p></div>
<div class="project" style="left:420px"><div class="project__img" style="background:linear-gradient(#f5f5f5,#b9bcc0)" role="img" aria-label="Arthroscopy console and handpiece photo"></div><p class="project__text" style="padding-top:40px">5 complete arthroscopy systems, supplied for 5 hospitals mostly in Baghdad.</p></div>
<div class="project" style="left:786px"><div class="project__img" style="background:linear-gradient(#eef1f6,#3d4f86)" role="img" aria-label="Automated ELISA analyzer photo"></div><p class="project__text" style="padding-top:40px">Full Automated Elisa System (Selra Diagnostics)10 units.</p></div>
<i class="dot" style="left:543px;background:var(--navy)"></i>
<i class="dot" style="left:567px;background:var(--blue)"></i>
<i class="dot" style="left:591px;background:var(--navy)"></i>

<!-- contact -->
<section class="abs contact"></section>
<h2 class="abs contact__title">Have Any Question?</h2>
<div class="field" style="left:90px;top:3851px;width:204px;height:28px">Your Name</div>
<div class="field" style="left:315px;top:3851px;width:201px;height:28px">Your Phone</div>
<div class="field" style="left:90px;top:3898px;width:204px;height:30px">Email Address</div>
<div class="field" style="left:315px;top:3898px;width:201px;height:30px">Subject</div>
<div class="field" style="left:90px;top:3947px;width:426px;height:100px">Your Message</div>
<div class="btn btn--blue" style="left:88px;top:4067px;width:426px;height:42px;font-size:14px;font-weight:600">GET IN TOUCH WITH US</div>
<div class="abs" style="left:563px;top:3732px;width:564px;height:441px;background:linear-gradient(135deg,#eef0f2,#e2ebe0)" role="img" aria-label="Street map showing the office location"></div>

<!-- footer -->
<svg class="abs" style="left:0;top:4240px" width="1200" height="180" aria-hidden="true">
  <path d="M0 150 C300 40 600 10 1200 60 L1200 180 L0 180Z" fill="var(--navy)"/>
  <path d="M0 160 C320 60 650 40 1200 80 L1200 180 L0 180Z" fill="var(--blue)"/>
  <path d="M0 180 C330 85 680 70 1200 100 L1200 180Z" fill="var(--black)"/>
</svg>
<footer class="abs" style="left:0;top:4420px;width:1200px;height:431px;background:var(--black)"></footer>
<div class="brand" style="left:81px;top:4520px;color:var(--blue-mid)">
  <div class="brand__mark" style="width:50px;height:50px"></div>
  <div><span class="brand__name" style="font-size:30px">Zerovan Medical</span><span class="brand__tag">FOR MEDICAL APPLIANCES</span></div>
</div>
<p class="abs footer__text">ZEROVAN MEDICAL Company is one of the specialized private companies in Iraq. Our job fields are lab. Diagnostics, equipment and medical appliances &amp; Ophthalmic Dept.</p>
<div class="flink" style="top:4535px"><span>HOME</span></div>
<div class="flink" style="top:4571px"><span>ABOUT</span></div>
<div class="flink" style="top:4607px"><span>SERVICES</span></div>
<div class="flink" style="top:4643px"><span>PROJECTS</span></div>
<div class="flink" style="top:4679px"><span>CONTACT</span></div>
<svg class="abs" style="left:872px;top:4545px" width="24" height="130" aria-hidden="true">
  <path d="M4 3 l5 0 l2 6 l-3 2 c1 3 3 5 6 6 l2-3 l6 2 l0 5 c-10 1 -19 -8 -18 -18z" fill="var(--blue)"/>
  <rect x="2" y="55" width="20" height="14" fill="var(--blue)"/><path d="M2 55 l10 8 l10-8" stroke="var(--black)" stroke-width="2" fill="none"/>
  <path d="M12 100 a7 7 0 0 1 7 7 c0 6 -7 13 -7 13 c0 0 -7 -7 -7 -13 a7 7 0 0 1 7-7z" fill="var(--blue)"/><circle cx="12" cy="107" r="2.5" fill="var(--black)"/>
</svg>
<div class="fcontact" style="top:4547px">(+964) 750 214 0387</div>
<div class="fcontact" style="top:4596px">support@zerovanmed.example</div>
<div class="fcontact" style="top:4645px">Sarwaran St. 14, Erbil</div>
<div class="abs footer__rule"></div>
<div class="abs footer__small" style="left:81px">Copyright 2024, All Rights Reserved.</div>
<div class="abs footer__small" style="left:862px">Privacy Policy | Term and Conditions</div>

</body>
</html>
```